Solar Company Solution Brochures

We are looking for a brochure design and theme that we can use moving forward. We are a solar microgrid company in New Zealand. We sell solar solutions and want a brochure for our most common solution. I have many other images and information so do ask. Solution diagram is shown and parts involved are also included. I dont want pricing on brochure.
Further work will be available to winner.

Target Market(s)

Offgrid solar customers.

Industry/Entity Type

Solar Energy

```html
<!DOCTYPE html>
<html lang="en">
<head>
<meta charset="UTF-8">
<title>Kestrel Grid – Back Cover</title>
<link rel="stylesheet" href="https://fonts.googleapis.com/css2?family=Montserrat:wght@300;400;500;700&display=swap">
<style>
  :root {
    --blue-light: #1789d4;
    --blue-mid: #1380cc;
    --blue-deep: #0e73bd;
    --ink: #0c1c2c;
    --navy: #0f2b47;
    --white: #ffffff;
  }
  * { margin: 0; padding: 0; box-sizing: border-box; }
  html, body {
    width: 927px;
    height: 1200px;
    overflow: hidden;
    background: var(--blue-mid);
  }
  .back-cover {
    position: relative;
    width: 927px;
    height: 1200px;
    overflow: hidden;
    font-family: 'Montserrat', sans-serif;
  }
  .hero-photo {
    position: absolute;
    inset: 0;
    background: linear-gradient(160deg, var(--blue-light) 0%, var(--blue-mid) 45%, var(--blue-deep) 100%);
  }
  .brand {
    position: absolute;
    left: 0;
    right: 0;
    top: 578px;
    display: flex;
    justify-content: center;
    align-items: center;
    gap: 12px;
  }
  .brand-mark {
    width: 22px;
    height: 22px;
    background: var(--ink);
  }
  .brand-name {
    font-size: 38px;
    font-weight: 500;
    letter-spacing: 1px;
    color: var(--ink);
  }
  .tagline {
    position: absolute;
    left: 0;
    right: 0;
    top: 870px;
    text-align: center;
  }
  .tagline-title {
    font-size: 22px;
    font-weight: 700;
    color: var(--navy);
    letter-spacing: 0.3px;
  }
  .tagline-text {
    margin-top: 18px;
    font-size: 19.5px;
    font-weight: 400;
    line-height: 24px;
    color: var(--white);
    letter-spacing: 0.4px;
  }
  .contact {
    position: absolute;
    left: 0;
    right: 0;
    top: 1084px;
    text-align: center;
  }
  .contact-phone {
    font-size: 37px;
    font-weight: 700;
    color: var(--white);
    letter-spacing: 0.5px;
  }
  .contact-web {
    margin-top: 12px;
    font-size: 19px;
    font-weight: 500;
    color: var(--navy);
    letter-spacing: 0.6px;
  }
</style>
</head>
<body>
  <main class="back-cover">
    <div class="hero-photo" role="img" aria-label="Blue-tinted photo of stacked lithium battery storage units on a rack"></div>

    <div class="brand">
      <span class="brand-mark"></span>
      <span class="brand-name">Kestrel Grid</span>
    </div>

    <section class="tagline">
      <h2 class="tagline-title">LIBERO TEMPORE</h2>
      <p class="tagline-text">numquam eius modi tempora<br>incidunt ut labore et dolore</p>
    </section>

    <section class="contact">
      <p class="contact-phone">500 810 370 640</p>
      <p class="contact-web">WWW.KESTRELGRID.COM</p>
    </section>
  </main>
</body>
</html>
```